Clockharbor Homepage Banner 1060 W x 100 H

Please see the attached 'word' document (Also copied below)
Feel free to use any images or logos from our website.
www.clockharbor.com.au

Background:
We are an Australian based official watch distributor/online retailer of international watch brands.

We require a new banner ad (1060 W x 100 H) to replace the existing one on our homepage www.clockharbor.com.au & wish to convey the following information:
*(Please feel free to alter wording, include or exclude points below & generally take creative license (with commercial reality in mind). We sell some luxury watches, so it must look professional & maintain a luxury look & feel.)

Clockharbor Direct:
Revolutionising the retail watch market !

- Buy direct from the official distributor & get world competitive
online prices (with full international warranty, & all original
papers, box & invoice)

- Eliminate all risk of fakes & non-existent factory warranty from
'grey' market sellers

- Free worldwide delivery over A$300

- Order online & 'try-on' in the comfort of your own home.
If you're not 100% happy, just post it back for a full refund or
exchange within 30 days

- Prefer to see & try on before purchase? Visit one of our retail
partner stores.

*** Feel free to copy any images from our website
www.clockharbor.com.au
Updates

Target Market(s)

Luxury watches

Industry/Entity Type

Retail

Font styles to use
Sans Serif

Requirements
Must have
• Visual imagery, text
Nice to have
• Feel free to use your creativity...
Should not have
• Cheap looking or tacky images. We sell some luxury watches, so we need to keep a professional & luxury image.

```html
<!DOCTYPE html>
<html lang="en">
<head>
<meta charset="utf-8">
<title>Clockharbor Direct – Homepage Banner</title>
<link rel="stylesheet" href="https://fonts.googleapis.com/css2?family=Arimo:wght@400;700&family=Roboto+Condensed:wght@700&display=swap">
<style>
  :root {
    --bg-dark: #0c0c0e;
    --bg-mid: #2a2a2e;
    --gold: #c9a560;
    --gold-light: #e0c48a;
    --white: #ffffff;
    --navy: #0d2a6b;
    --navy-deep: #08194a;
    --red: #c8101c;
    --red-deep: #9c0a12;
    --yellow: #ffe84a;
    --photo-steel: #8d949c;
    --photo-blue: #1b2f66;
  }
  * { margin: 0; padding: 0; box-sizing: border-box; }
  html, body { width: 1200px; height: 113px; overflow: hidden; background: var(--bg-dark); }
  .banner {
    position: relative;
    width: 1200px;
    height: 113px;
    overflow: hidden;
    background: linear-gradient(90deg, var(--bg-dark) 0%, var(--bg-mid) 55%, var(--bg-dark) 75%);
    font-family: "Arimo", Arial, sans-serif;
  }
  .product-photo {
    position: absolute;
    left: 0; top: 0;
    width: 272px; height: 113px;
    background: radial-gradient(circle at 150px 40px, var(--photo-blue) 0%, var(--photo-blue) 38%, var(--photo-steel) 48%, #3b3f45 75%, var(--bg-dark) 100%);
  }
  .divider {
    position: absolute;
    left: 276px; top: 0;
    width: 3px; height: 113px;
    background: linear-gradient(180deg, var(--gold-light), var(--gold));
  }
  .headline {
    position: absolute;
    left: 296px; top: 4px;
    font-family: "Roboto Condensed", "Arial Narrow", sans-serif;
    font-weight: 700;
    font-size: 37px;
    line-height: 1;
    letter-spacing: 0.5px;
    color: var(--gold);
  }
  .pitch {
    position: absolute;
    left: 296px; top: 45px;
    width: 420px;
    font-size: 15px;
    line-height: 17px;
    color: var(--white);
  }
  .offer-shape { position: absolute; left: 0; top: 0; }
  .offer-discount {
    position: absolute;
    left: 900px; top: 22px;
    width: 300px;
    text-align: center;
    color: var(--white);
    font-size: 19px;
    line-height: 1;
  }
  .offer-discount strong { font-size: 30px; font-weight: 700; }
  .offer-delivery {
    position: absolute;
    left: 880px; top: 82px;
    width: 320px;
    text-align: center;
    color: var(--yellow);
    font-weight: 700;
    font-size: 16px;
  }
</style>
</head>
<body>
<div class="banner">
  <div class="product-photo" role="img" aria-label="Close-up photo of a luxury diver's watch with a blue dial"></div>
  <div class="divider"></div>

  <h1 class="headline">BUY DIRECT</h1>
  <p class="pitch">From the official distributor &amp; get world competitive online prices! (with full international warranty, &amp; all original papers, box &amp; invoice)</p>

  <svg class="offer-shape" width="1200" height="113" viewBox="0 0 1200 113" aria-hidden="true">
    <defs>
      <linearGradient id="navyFill" x1="0" y1="0" x2="0" y2="1">
        <stop offset="0" stop-color="var(--navy)"/>
        <stop offset="1" stop-color="var(--navy-deep)"/>
      </linearGradient>
      <linearGradient id="redFill" x1="0" y1="0" x2="0" y2="1">
        <stop offset="0" stop-color="var(--red)"/>
        <stop offset="1" stop-color="var(--red-deep)"/>
      </linearGradient>
    </defs>
    <path d="M870 0 C 905 25, 870 80, 830 113 L1200 113 L1200 0 Z" fill="url(#navyFill)"/>
    <path d="M862 0 C 897 25, 862 80, 822 113" fill="none" stroke="var(--gold-light)" stroke-width="3"/>
    <path d="M860 76 C 960 72, 1100 66, 1200 62 L1200 113 L836 113 Z" fill="url(#redFill)"/>
    <path d="M860 76 C 960 72, 1100 66, 1200 62" fill="none" stroke="var(--white)" stroke-width="2"/>
  </svg>

  <p class="offer-discount">UP TO <strong>50% OFF!</strong></p>
  <p class="offer-delivery">Free worldwide delivery over A$300</p>
</div>
</body>
</html>
```